Modern Label for cleaning products for the brand Voralux

We need a label design for our line of cleaning products. The label should feature our logo and an image to identify the product's intended use. I've added our logo and an image for use. This only concerns the design of the label on the front of the bottle.

Label dimensions:
Label 1 (500ml bottle with spray): width 58mm x height 115mm
Label 2: (1L bottle): width 73mm x height 140mm
The design must be consistent for both bottles which you find in the pictures.

The bottles to be labeled are white. See the attachment for a photo of the bottles.

The photo must also appear on the label to identify the product's intended use.

Product information:
Brand: Voralux
Product: Sanitary Cleaner

This text must be placed on the label:
"Cleans, descales & freshens. followed with this text: "Ideal for quick and powerful cleaning. A ready-to-use product for everyday use."

- Mention the seperate USP's: Sanitary, Bathroom, Toilet, Wet areas

Appearance: This is a consumer product, but it must have a professional appearance. We would like to see a design that use the color blue from our logo.

Target Market(s)

Consumers who take care of their homes and want to maintain it the correct (professional) way

Font styles to use
Sans Serif

Colors
0054AA
0677BA
7BADD7
CADEEF
E8F1F8

Requirements
Must have
• USP's + use of image and logo + blend in 1 design
Nice to have
• Keep the color of the logo in the design
Should not have
• Comic sans

```html
<!DOCTYPE html>
<html lang="en">
<head>
<meta charset="UTF-8">
<title>Voralux Sanitary Cleaner – Labels</title>
<link rel="stylesheet" href="https://fonts.googleapis.com/css2?family=Oswald:wght@500;600&family=Roboto+Condensed:wght@500;700&display=swap">
<style>
  :root{
    --page:#ffffff;
    --royal:#0b3ccf;
    --royal-mid:#1f5fe0;
    --brand-blue:#0054AA;
    --navy:#0a2a7a;
    --band:#0d3fb4;
    --sky:#2a9ce8;
    --sky-light:#3cbcf6;
    --mist:#CADEEF;
    --ice:#E8F1F8;
    --white:#ffffff;
    --usp:#0a2f86;
  }
  *{box-sizing:border-box;margin:0;padding:0}
  html,body{width:720px;height:1200px;overflow:hidden;background:var(--page)}
  .sheet{
    width:720px;height:1200px;
    display:flex;align-items:flex-end;justify-content:center;gap:30px;
    padding-bottom:250px;
  }
  .label{
    position:relative;overflow:hidden;
    border-radius:0.9em;
    background:linear-gradient(180deg,var(--royal) 0%,var(--royal-mid) 40%,var(--sky) 79%,var(--sky-light) 100%);
    font-family:"Roboto Condensed",sans-serif;
    color:var(--white);
    text-align:center;
  }
  .label--500{width:290px;height:575px;font-size:14.5px}
  .label--1l{width:365px;height:700px;font-size:18.25px}

  .glow{
    position:absolute;left:50%;top:30%;width:22em;height:14em;
    transform:translate(-50%,-50%);
    background:radial-gradient(ellipse at center,rgba(255,255,255,.85) 0%,rgba(255,255,255,.35) 18%,rgba(255,255,255,0) 60%);
  }
  .scene{
    position:absolute;left:0;right:0;top:34%;height:40%;
    background:
      linear-gradient(180deg,rgba(31,95,224,.9) 0%,rgba(31,95,224,0) 28%,rgba(13,63,180,0) 80%,rgba(13,63,180,.6) 100%),
      linear-gradient(90deg,#6f86b8 0%,#c9cfd8 25%,#e9ebee 50%,#c4c9d1 75%,#7d90ba 100%);
  }
  .brand{position:absolute;left:0;right:0;top:4.5%;display:flex;flex-direction:column;align-items:center;gap:0.55em}
  .brand__dot{width:5.2em;height:5.2em;border-radius:50%;background:var(--white)}
  .brand__name{font-weight:700;font-size:2.1em;letter-spacing:.01em;line-height:1}

  .title{
    position:absolute;left:0;right:0;top:35%;
    font-family:"Oswald",sans-serif;font-weight:600;
    font-size:3.5em;line-height:1.08;text-transform:uppercase;letter-spacing:.01em;
    color:var(--white);
    text-shadow:0 0 0.06em var(--navy),0.04em 0.04em 0 var(--navy),-0.04em -0.04em 0 var(--navy),0.04em -0.04em 0 var(--navy),-0.04em 0.04em 0 var(--navy),0.06em 0.09em 0.08em rgba(0,20,80,.6);
  }
  .claim{
    position:absolute;left:0;right:0;top:73.5%;height:6%;
    display:flex;align-items:center;justify-content:center;
    background:linear-gradient(90deg,rgba(13,63,180,.55),var(--band) 20%,var(--band) 80%,rgba(13,63,180,.55));
    font-family:"Oswald",sans-serif;font-weight:500;font-size:1.15em;text-transform:uppercase;
  }
  .info{position:absolute;left:0;right:0;top:82%;font-family:"Oswald",sans-serif;font-weight:500;font-size:0.82em;line-height:1.6;text-transform:uppercase}
  .usps{position:absolute;left:0;right:0;top:90.5%;font-weight:700;font-size:0.82em;color:var(--usp)}
  .volume{position:absolute;left:0;right:0;top:95.5%;font-weight:500;font-size:0.62em;color:var(--ice)}
</style>
</head>
<body>
<main class="sheet">
  <article class="label label--500">
    <div class="scene" role="img" aria-label="Photo of a bright, clean modern bathroom"></div>
    <div class="glow"></div>
    <div class="brand"><span class="brand__dot"></span><span class="brand__name">voralux</span></div>
    <h1 class="title">Sanitary<br>Cleaner</h1>
    <p class="claim">Cleans, descales &amp; freshens.</p>
    <p class="info">Ideal for quick and powerful cleaning.<br>A ready-to-use product for everyday use.</p>
    <p class="usps">Sanitary, Bathroom, Toilet, Wet areas.</p>
    <p class="volume">500ml</p>
  </article>
  <article class="label label--1l">
    <div class="scene" role="img" aria-label="Photo of a bright, clean modern bathroom"></div>
    <div class="glow"></div>
    <div class="brand"><span class="brand__dot"></span><span class="brand__name">voralux</span></div>
    <h1 class="title">Sanitary<br>Cleaner</h1>
    <p class="claim">Cleans, descales &amp; freshens.</p>
    <p class="info">Ideal for quick and powerful cleaning.<br>A ready-to-use product for everyday use.</p>
    <p class="usps">Sanitary, Bathroom, Toilet, Wet areas.</p>
    <p class="volume">1L</p>
  </article>
</main>
</body>
</html>
```